Therapy Services & Training

I provide counseling/therapy to individuals and families. I also travel the country and provide training at conferences.
I would like to see a card which takes my company name and design a logo using the letters "MCAC".
Target Market(s)
Therapists, non-profit organizations, clients looking for therapy
Industry/Entity Type
Training
Contact Information for Business Card
Meridel Clinical Advising & Coaching LLC
Danelle Brooks, M.S.W., LCSW
Clinical Therapist & Trainer
Providing clinical therapy services to individuals, families, couples & children. We also provide life coaching and crisis training.
helpdeskdanelle@mailbrook.example
www.meridelclinicaladvising.example
(555) 214-0397
Brookvale, IL 60000
(BACK SIDE OF CARD)
We are certified by the Baseline Ongoing Lawyer Instruction (BOLI) Panel of the Statewide High Tribunal to provide Continuing Legal Education (CLE) credits to Illinois attorneys. Call about what courses we offer! (555) 214-0397

```html
<!DOCTYPE html>
<html lang="en">
<head>
<meta charset="utf-8">
<title>MCAC Business Card</title>
<link rel="stylesheet" href="https://fonts.googleapis.com/css2?family=Questrial&family=Poppins:wght@600&family=Open+Sans:ital,wght@1,700&family=Tinos:ital,wght@0,400;1,700&display=swap">
<style>
  :root {
    --board: #c9b98f;
    --board-deep: #a89a6e;
    --banner: #f3ecc4;
    --ink: #111111;
    --card: #0aa0c4;
    --hands: #5fb7cf;
    --rule: #8fd3e6;
    --white: #ffffff;
  }
  * { margin: 0; padding: 0; box-sizing: border-box; }
  html, body { width: 927px; height: 1200px; overflow: hidden; }
  body { position: relative; background: var(--board); font-family: "Questrial", sans-serif; }

  .board-pattern {
    position: absolute; inset: 0;
    background: radial-gradient(ellipse at 50% 45%, var(--board) 40%, var(--board-deep) 100%);
  }
  .sheet-title {
    position: absolute; left: 0; top: 22px; width: 620px; height: 62px;
    background: var(--banner);
    font-family: "Tinos", serif; font-size: 52px; line-height: 62px;
    padding-left: 26px; color: var(--ink);
  }
  .side-label {
    position: absolute; font-family: "Tinos", serif; font-size: 46px; color: var(--ink);
    transform: translate(-50%, -50%) rotate(-90deg); white-space: nowrap;
  }
  .side-label.front { left: 110px; top: 360px; }
  .side-label.back { left: 110px; top: 877px; }
  .sheet-note {
    position: absolute; left: 0; width: 927px; top: 1150px; text-align: center;
    font-family: "Tinos", serif; font-style: italic; font-weight: 700; font-size: 30px; color: var(--ink);
  }

  .card {
    position: absolute; left: 170px; width: 662px; height: 388px;
    background: var(--card); color: var(--white); overflow: hidden;
  }
  .card.front { top: 185px; }
  .card.back { top: 670px; }
  .hands-photo {
    position: absolute; opacity: .55;
    background: radial-gradient(ellipse at center, var(--hands) 0%, var(--card) 70%);
  }
  .front .hands-photo { left: 40px; top: 40px; width: 320px; height: 300px; }
  .back .hands-photo { left: 130px; top: 0; width: 420px; height: 240px; }
  .rules { position: absolute; left: 0; top: 0; }

  .wordmark {
    position: absolute; left: 40px; top: 30px;
    font-size: 58px; line-height: 70px; color: var(--white);
  }
  .company {
    position: absolute; left: 240px; width: 380px; top: 38px; text-align: center;
    font-family: "Open Sans", sans-serif; font-style: italic; font-weight: 700;
    font-size: 20.5px; line-height: 30px;
  }
  .person {
    position: absolute; left: 0; width: 662px; top: 140px; text-align: center;
    font-size: 29px; line-height: 40px; font-weight: 400;
  }
  .services {
    position: absolute; left: 116px; width: 430px; top: 198px; text-align: center;
    font-size: 17.5px; line-height: 24px;
  }
  .contact-line {
    position: absolute; left: 0; width: 662px; top: 344px; text-align: center;
    font-style: italic; font-size: 12px;
  }

  .accreditation {
    position: absolute; left: 78px; width: 506px; top: 60px; text-align: center;
    font-family: "Poppins", sans-serif; font-weight: 600; font-size: 20.5px; line-height: 30px;
  }
  .call-out {
    position: absolute; left: 0; width: 662px; top: 243px; text-align: center;
    font-style: italic; font-size: 20px; line-height: 30px;
  }
</style>
</head>
<body>
  <div class="board-pattern" role="img" aria-label="Tan parchment presentation board with a large olive damask scroll pattern"></div>

  <div class="sheet-title">MCAC Business Card</div>
  <div class="side-label front">Front Side</div>
  <div class="side-label back">Back Side</div>

  <section class="card front">
    <div class="hands-photo" role="img" aria-label="Faint photo of two open cupped hands"></div>
    <svg class="rules" width="662" height="388" viewBox="0 0 662 388" aria-hidden="true">
      <g stroke="var(--rule)" stroke-width="3">
        <line x1="255" y1="63" x2="662" y2="63"/>
        <line x1="98" y1="182" x2="552" y2="182"/>
      </g>
    </svg>
    <div class="wordmark">MCAC</div>
    <div class="company">Meridel Clinical Advising &amp;<br>Coaching LLC</div>
    <h1 class="person">Danelle Brooks, M.S.W., LCSW</h1>
    <p class="services">Clinical Therapist &amp; Trainer Providing clinical therapy services to individuals, families, couples &amp; children. We also provide life coaching and crisis training.</p>
    <p class="contact-line">helpdeskdanelle@mailbrook.example • www.meridelclinicaladvising.example • (555) 214-0397 • Brookvale, IL 60000</p>
  </section>

  <section class="card back">
    <div class="hands-photo" role="img" aria-label="Faint photo of two open cupped hands"></div>
    <svg class="rules" width="662" height="388" viewBox="0 0 662 388" aria-hidden="true">
      <g stroke="var(--rule)" stroke-width="3">
        <line x1="0" y1="221" x2="662" y2="221"/>
        <line x1="47" y1="236" x2="615" y2="236"/>
      </g>
    </svg>
    <p class="accreditation">We are certified by the Baseline Ongoing Lawyer Instruction (BOLI) Panel of the Statewide High Tribunal to provide Continuing Legal Education (CLE) credits to Illinois attorneys.</p>
    <p class="call-out">Call about what courses we offer!<br>(555) 214-0397</p>
  </section>

  <div class="sheet-note">Please Note: Background is not part of the design....</div>
</body>
</html>
```